IT Freelancer (Consulting, trainer and project manager) needed letterhead

As a freelancer for IT Trainingswhip, consulting and project management I need a letterhead design. What is desired is a design that fits the existing logo (see Annex). It is functional, reliable, and equal time wirkenn Agil and modern. The whole is in color, as well as printed out to make a good impression on a black and white printer. The whole is to the existing Cooperate design (business card, homepage, logo) fit. Therefore, the choice of colors.
Updates

Target Market(s)

Customers such as medium-sized enterprises, training institutions

Industry/Entity Type

Consulting

Colors
0455a3
3277b5
85abd2
cfdfed
34a6d7
32a6d6
249fd4
0792cd
85cae6

Requirements
Must have
• Must include logo (see Annex) address (Brennerweg 14, 92637 Weiden, Germany). Must seriously and act simultaneously Agil. Design should (even) be adaptable (signature, address, etc.) design must look good on a black / white laser

```html
<!DOCTYPE html>
<html lang="en">
<head>
<meta charset="utf-8">
<title>Lukas Renner – Letterhead</title>
<link rel="stylesheet" href="https://fonts.googleapis.com/css2?family=Source+Sans+3:wght@400;700&display=swap">
<style>
  :root {
    --blue-deep: #0455a3;
    --blue-mid: #3277b5;
    --blue-bright: #0792cd;
    --blue-light: #85cae6;
    --ink: #1c1c1c;
    --paper: #ffffff;
  }
  * { margin: 0; padding: 0; box-sizing: border-box; }
  html, body { width: 1116px; height: 1200px; overflow: hidden; background: var(--paper); }
  body { font-family: "Source Sans 3", Arial, sans-serif; color: var(--ink); }
  .letterhead { position: relative; width: 1116px; height: 1200px; background: var(--paper); overflow: hidden; }

  .corner-accent { position: absolute; }
  .corner-accent-top { right: 0; top: 0; width: 200px; height: 190px;
    background: linear-gradient(225deg, var(--blue-deep) 0%, var(--blue-bright) 55%, rgba(133,202,230,0) 100%); }
  .corner-accent-bottom { left: 0; bottom: 0; width: 230px; height: 190px;
    background: linear-gradient(45deg, var(--blue-deep) 0%, var(--blue-bright) 55%, rgba(133,202,230,0) 100%); }

  .brand { position: absolute; left: 150px; top: 42px; width: 200px; text-align: center; }
  .brand-dot { width: 124px; height: 124px; border-radius: 50%; background: var(--blue-bright); margin: 0 auto 20px; }
  .brand-name { font-size: 28px; font-weight: 700; color: var(--blue-deep); letter-spacing: 1px; line-height: 1.05; text-transform: uppercase; }

  .recipient { position: absolute; left: 148px; top: 336px; }
  .recipient-name { font-size: 20px; line-height: 1.2; }
  .recipient-line { font-size: 13px; line-height: 1.35; }

  .body-copy { position: absolute; left: 148px; width: 866px; font-size: 13.8px; line-height: 16.4px; text-align: justify; }
  .para-1 { top: 441px; }
  .para-2 { top: 636px; }
  .para-3 { top: 766px; }

  .closing { position: absolute; left: 840px; top: 906px; }
  .closing-word { font-size: 13px; }
  .closing-name { font-size: 21px; line-height: 1.2; }

  .contact-list { position: absolute; left: 250px; top: 1080px; list-style: none; font-size: 15px; line-height: 19px; }
  .contact-list li { display: flex; align-items: center; gap: 8px; }
  .contact-icon { width: 13px; height: 13px; flex: none; }
  .address { position: absolute; left: 440px; top: 1082px; font-size: 15px; line-height: 19px; }
</style>
</head>
<body>
<main class="letterhead">
  <div class="corner-accent corner-accent-top" role="img" aria-label="Blue angular corner accent"></div>
  <div class="corner-accent corner-accent-bottom" role="img" aria-label="Blue angular corner accent"></div>

  <header class="brand">
    <div class="brand-dot"></div>
    <div class="brand-name">Lukas<br>Renner</div>
  </header>

  <section class="recipient">
    <p class="recipient-name">Mr. Daniel Hartley</p>
    <p class="recipient-line">Managing Director</p>
    <p class="recipient-line">Northfield Business Center</p>
  </section>

  <p class="body-copy para-1">Maecenas non rutrum libero. Donec odio lorem, vehicula eu fermentum ut, varius vel purus. Sed varius faucibus enim eu tincidunt. Nullam accumsan metus elit, et blandit risus tincidunt id. Etiam laoreet ultricies est, eu venenatis orci pharetra quis. Cras ut efficitur massa. Mauris nec sodales libero, id pretium quam. Mauris et nulla nec nunc imperdiet ultricies. Sed suscipit, felis eget dignissim luctus, erat nisl euismod nibh, in dignissim nisl est et neque. Proin bibendum quis felis id dignissim. Nulla vitae elementum neque. Nam sollicitudin felis dui, quis consectetur elit accumsan a. Maecenas eget erat eleifend, fermentum metus vel, mattis nunc. Duis at rutrum ligula, sit amet finibus arcu. Aliquam lacus nulla, molestie id porta gravida, rutrum molestie nisi. Proin volutpat nisl ac pharetra dictum. Curabitur sed quam ex. Ut pellentesque pulvinar purus, at sagittis arcu porttitor eu. Nam suscipit vestibulum blandit. Ut tempus ante sed arcu sollicitudin, non hendrerit sem porttitor. In congue in justo ut vehicula. Sed pellentesque felis ut velit placerat, ut tristique massa vestibulum. Integer viverra, massa eget scelerisque tempus, magna quam convallis nibh, vel consectetur turpis diam vitae nisl. Donec lobortis placerat dolor.</p>

  <p class="body-copy para-2">Nullam accumsan metus elit, et blandit risus tincidunt id. Etiam laoreet ultricies est, eu venenatis orci pharetra quis. Cras ut efficitur massa. Mauris nec sodales libero, id pretium quam. Mauris et nulla nec nunc imperdiet ultricies. Sed suscipit, felis eget dignissim luctus, erat nisl euismod nibh, in dignissim nisl est et neque. Proin bibendum quis felis id dignissim. Nulla vitae elementum neque. Nam sollicitudin felis dui, quis consectetur elit accumsan a. Maecenas eget erat eleifend, fermentum metus vel, mattis nunc. Duis at rutrum ligula, sit amet finibus arcu. Aliquam lacus nulla, molestie id porta gravida, rutrum molestie nisi. Proin volutpat nisl ac pharetra dictum. Curabitur sed quam ex accumsan eget erat.</p>

  <p class="body-copy para-3">Nullam accumsan metus elit, et blandit risus tincidunt id. Etiam laoreet ultricies est, eu venenatis orci pharetra quis. Cras ut efficitur massa. Mauris nec sodales libero, id pretium quam. Mauris et nulla nec nunc imperdiet ultricies. Sed suscipit, felis eget dignissim luctus, erat nisl euismod nibh, in dignissim nisl est et neque. Proin bibendum quis felis id dignissim. Nulla vitae elementum neque. Nam sollicitudin felis dui, quis consectetur elit accumsan.</p>

  <section class="closing">
    <p class="closing-word">Sincerely</p>
    <p class="closing-name">Markus Feldt</p>
  </section>

  <footer>
    <ul class="contact-list">
      <li>
        <svg class="contact-icon" viewBox="0 0 16 16" aria-hidden="true"><circle cx="8" cy="8" r="8" fill="var(--blue-light)"/><path d="M5 4.5c.6-.5 1.2-.3 1.5.3l.6 1.2c.2.4 0 .8-.3 1l-.5.4c.4 1 1.1 1.7 2 2.1l.4-.5c.3-.3.7-.4 1-.2l1.2.6c.6.3.7.9.3 1.5-.6.8-1.6 1-2.6.5C6.8 10.5 5.6 9.3 4.7 7.5 4.2 6.5 4.3 5.2 5 4.5z" fill="var(--blue-deep)"/></svg>
        88-456-210734
      </li>
      <li>
        <svg class="contact-icon" viewBox="0 0 16 16" aria-hidden="true"><circle cx="8" cy="8" r="8" fill="var(--blue-light)"/><rect x="4" y="5" width="8" height="6" rx="1" fill="var(--blue-deep)"/><path d="M4.5 5.6 8 8.3l3.5-2.7" stroke="#fff" stroke-width=".8" fill="none"/></svg>
        hello@renner-it.com
      </li>
      <li>
        <svg class="contact-icon" viewBox="0 0 16 16" aria-hidden="true"><circle cx="8" cy="8" r="7.5" fill="var(--blue-light)"/><g stroke="var(--blue-deep)" stroke-width=".9" fill="none"><circle cx="8" cy="8" r="5"/><ellipse cx="8" cy="8" rx="2.2" ry="5"/><path d="M3 8h10"/></g></svg>
        www.renner-it.com
      </li>
    </ul>
    <p class="address">Brennerweg 14, 92637 Weiden,<br>Germany</p>
  </footer>
</main>
</body>
</html>
```